Business Card Design needed for logo design project

Our company needs a Business Card Design. Please refer to our original project in the link above.

Industry/Entity Type

Business

```html
<!DOCTYPE html>
<html lang="en">
<head>
<meta charset="utf-8">
<title>quovelli — Business Card</title>
<link href="https://fonts.googleapis.com/css2?family=Questrial&display=swap" rel="stylesheet">
<style>
  :root {
    --backdrop: #e8e5e1;
    --card: #ffffff;
    --ink: #111111;
    --icon: #555555;
    --band: #7d7d7d;
    --band-text: #d6d6d6;
    --rule: #e2e2e2;
  }
  * { margin: 0; padding: 0; box-sizing: border-box; }
  html, body {
    width: 1200px;
    height: 676px;
    overflow: hidden;
    background: var(--backdrop);
    font-family: "Questrial", "Century Gothic", sans-serif;
  }
  .card {
    position: absolute;
    left: 110px;
    top: 58px;
    width: 980px;
    height: 560px;
    background: var(--card);
    box-shadow: 0 6px 24px rgba(0, 0, 0, 0.12);
    overflow: hidden;
  }
  .brand-name {
    position: absolute;
    left: 290px;
    top: 48px;
    font-size: 132px;
    line-height: 1;
    letter-spacing: 4px;
    color: var(--ink);
    white-space: nowrap;
  }
  .holder-name {
    position: absolute;
    left: 110px;
    top: 222px;
    font-size: 28px;
    letter-spacing: 1px;
    color: var(--ink);
  }
  .brand-rule {
    position: absolute;
    left: 180px;
    top: 270px;
    width: 560px;
    height: 1px;
    background: var(--rule);
  }
  .phone {
    position: absolute;
    left: 600px;
    top: 296px;
    display: flex;
    align-items: center;
    gap: 22px;
    font-size: 28px;
    color: var(--ink);
  }
  .phone svg { width: 20px; height: 28px; }
  .contact-band {
    position: absolute;
    left: 0;
    top: 372px;
    width: 100%;
    height: 150px;
    background: var(--band);
    padding: 18px 0 0 50px;
    display: flex;
    flex-direction: column;
    gap: 8px;
    color: var(--band-text);
    font-size: 26px;
  }
  .contact-row {
    display: flex;
    align-items: center;
    gap: 22px;
    height: 32px;
    white-space: nowrap;
  }
  .contact-row svg { width: 22px; height: 22px; flex: none; }
  .contact-row .gap { width: 40px; display: inline-block; }
</style>
</head>
<body>
  <div class="card">
    <div class="brand-name">quovelli</div>
    <div class="holder-name">YOUR NAME</div>
    <div class="brand-rule"></div>
    <div class="phone">
      <svg viewBox="0 0 22 30" aria-hidden="true">
        <path d="M6 3 C3 4 2 8 3 13 C4 19 8 25 12 27 C14 28 16 27 17 25 L14 20 L11 21 C9 18 8 15 8 12 L11 10 L9 4 Z" fill="var(--icon)"/>
      </svg>
      <span>555-310-4827</span>
    </div>
    <div class="contact-band">
      <div class="contact-row">
        <svg viewBox="0 0 24 24" aria-hidden="true">
          <path d="M12 2 C7.5 2 5 5.2 5 9 C5 14 12 22 12 22 C12 22 19 14 19 9 C19 5.2 16.5 2 12 2 Z" fill="var(--band-text)"/>
          <circle cx="12" cy="9" r="2.8" fill="var(--band)"/>
        </svg>
        <span>418 Linden Row<span class="gap"></span>Bay Area CA-75012</span>
      </div>
      <div class="contact-row">
        <svg viewBox="0 0 24 24" aria-hidden="true" fill="none" stroke="var(--band-text)" stroke-width="1.6">
          <circle cx="12" cy="12" r="9.5"/>
          <ellipse cx="12" cy="12" rx="4.2" ry="9.5"/>
          <line x1="2.5" y1="12" x2="21.5" y2="12"/>
          <line x1="4" y1="7" x2="20" y2="7"/>
          <line x1="4" y1="17" x2="20" y2="17"/>
        </svg>
        <span>www.quovelli-cards.test</span>
      </div>
      <div class="contact-row">
        <svg viewBox="0 0 24 24" aria-hidden="true" fill="none" stroke="var(--band-text)" stroke-width="1.6">
          <rect x="2.5" y="5" width="19" height="14"/>
          <polyline points="2.5,5 12,13 21.5,5"/>
        </svg>
        <span>hello@quovelli-cards.test</span>
      </div>
    </div>
  </div>
</body>
</html>
```